Dynamic Business Card for Sports Supplements Company

Hi! I'm looking for an awesome business card to match my existing sports supplement company. I have uploaded my current company logo and screenshot of the front page of my website.

I would like to have something dynamic and interesting and utilize the colors in the website - the reds and purples

The business card should be double sided and focus on a unique eye-catching design on the back and include all the relevant company info.

Most importantly, it should say somewhere: "Sign up on our website for a coupon code."

Target Market(s)

Mostly for women gym goers but it shouldn't be too feminine. It should be in keeping with the website design. It should flow and clearly be connected to it

Industry/Entity Type

Business

Contact Information for Business Card

Lorena K. Vasquez
CEO
LVasquez@Fortivanco.example
www.fortivanco.example
614.275.3081
P.O. Box 48317
Ashby, Vermont 22417

Sign up on our website for a coupon code

Font styles to use
Serif
Sans Serif
Other font styles liked:
• Novecento font family and "Fortivan" is in AR Destine font

Requirements
Must have
• One side should be a bold Fortivan logo design. Even just the symbol itself may be o.k. (see attached file)

```html
<!DOCTYPE html>
<html lang="en">
<head>
<meta charset="utf-8">
<title>Fortivan Business Card</title>
<link rel="stylesheet" href="https://fonts.googleapis.com/css2?family=Open+Sans:wght@400;600;700;800&family=Exo+2:wght@700&display=swap">
<style>
  :root {
    --page-bg: #eeeff1;
    --card-white: #fbfbfb;
    --ink: #2a2a2a;
    --ink-soft: #4a4a4a;
    --brand-red: #e3262b;
    --slate-dark: #2c3240;
    --slate-mid: #3f4656;
    --on-dark: #ffffff;
  }
  * { box-sizing: border-box; margin: 0; padding: 0; }
  html, body {
    width: 1200px; height: 900px; overflow: hidden;
    background: var(--page-bg);
    font-family: "Open Sans", Arial, sans-serif;
    color: var(--ink);
  }
  .card-set {
    position: absolute; top: 307px; left: 70px;
    display: flex; gap: 60px;
  }
  .card {
    position: relative; width: 500px; height: 286px;
    box-shadow: 0 14px 30px rgba(0,0,0,0.14), 0 2px 5px rgba(0,0,0,0.08);
  }
  /* Front */
  .card-front { background: var(--card-white); }
  .holder { position: absolute; top: 30px; left: 34px; }
  .holder-name {
    color: var(--brand-red); font-size: 17px; font-weight: 400;
    letter-spacing: 0.8px; text-transform: uppercase;
  }
  .holder-role { font-size: 11px; color: var(--ink-soft); margin-top: 2px; }
  .contact-list { position: absolute; top: 98px; left: 34px; list-style: none; }
  .contact-item {
    display: flex; align-items: center; gap: 7px;
    font-size: 11.5px; color: var(--ink-soft); line-height: 17px;
  }
  .contact-icon { width: 9px; height: 9px; fill: var(--brand-red); flex: none; }
  .brand-lockup {
    position: absolute; top: 156px; right: 40px; text-align: left;
  }
  .brand-row { display: flex; align-items: center; gap: 8px; }
  .brand-mark { width: 22px; height: 22px; background: var(--brand-red); }
  .brand-name {
    font-size: 32px; font-weight: 800; color: var(--ink);
    letter-spacing: 1px; text-transform: uppercase; line-height: 1;
  }
  .brand-tagline {
    font-size: 9.5px; letter-spacing: 2.6px; text-transform: uppercase;
    color: var(--ink-soft); margin-top: 5px; padding-left: 30px;
  }
  .mailing-address {
    position: absolute; right: 40px; bottom: 22px;
    font-size: 12px; line-height: 17px; color: var(--ink-soft);
    font-style: normal; text-align: left;
  }
  /* Back */
  .card-back {
    background: radial-gradient(ellipse at 45% 35%, var(--slate-mid), var(--slate-dark) 75%);
    color: var(--on-dark);
  }
  .back-brand {
    position: absolute; top: 96px; left: 0; right: 0;
    display: flex; justify-content: center; align-items: center; gap: 10px;
  }
  .back-brand .brand-mark { width: 26px; height: 26px; }
  .back-brand .brand-name { color: var(--on-dark); font-size: 40px; }
  .coupon-note {
    position: absolute; left: 0; right: 0; top: 182px; text-align: center;
    font-family: "Exo 2", "Open Sans", sans-serif; font-weight: 700;
    font-size: 11.5px; letter-spacing: 1.3px; text-transform: uppercase;
  }
</style>
</head>
<body>
<main class="card-set">
  <section class="card card-front" aria-label="Card front">
    <div class="holder">
      <p class="holder-name">Lorena K. Vasquez</p>
      <p class="holder-role">CEO</p>
    </div>
    <ul class="contact-list">
      <li class="contact-item">
        <svg class="contact-icon" viewBox="0 0 10 10"><path d="M2 0.5 L3.6 0.5 L4.3 2.8 L3.2 3.7 Q4.2 5.8 6.3 6.8 L7.2 5.7 L9.5 6.4 L9.5 8 Q9.5 9.5 8 9.5 Q0.5 9 0.5 2 Q0.5 0.5 2 0.5Z"/></svg>
        614.275.3081
      </li>
      <li class="contact-item">
        <svg class="contact-icon" viewBox="0 0 10 10"><path d="M0.5 2 H9.5 V8.5 H0.5Z M0.5 2 L5 5.5 L9.5 2" stroke="#fff" stroke-width="0.8"/></svg>
        LVasquez@Fortivanco.example
      </li>
      <li class="contact-item">
        <svg class="contact-icon" viewBox="0 0 10 10"><circle cx="5" cy="5" r="4.5"/><path d="M0.5 5 H9.5 M5 0.5 V9.5" stroke="#fff" stroke-width="0.7"/></svg>
        www.fortivanco.example
      </li>
    </ul>
    <div class="brand-lockup">
      <div class="brand-row">
        <span class="brand-mark"></span>
        <span class="brand-name">Fortivan</span>
      </div>
      <p class="brand-tagline">Your Performance Partner</p>
    </div>
    <address class="mailing-address">
      P.O. Box 48317<br>Ashby, Vermont 22417
    </address>
  </section>

  <section class="card card-back" aria-label="Card back">
    <div class="back-brand">
      <span class="brand-mark"></span>
      <span class="brand-name">Fortivan</span>
    </div>
    <p class="coupon-note">Sign up on our website for a coupon code</p>
  </section>
</main>
</body>
</html>
```